Wordpress Design Project for MLG

We need a clean word press design for a new event planning company called Marigold Logistics & Gatherings. We assist planners or leaders who are in charge of planning conferences, meetings, or conventions. In addition, we offer small business development strategy. We do not decorate: we help clients negotiate better contracts and/ or develop better systems to become more efficient. I want people to come to this site for referrals for other businesses and for training information.
I would like to see a design that uses the colors in the logo. The final design should be creative, professional, and innovative.
Updates
Industry/Entity Type
Event Planning
Requirements
Must have
- user friendly! easy to Navigate!
I like the feel of the following websites:
http://www.ventureroost.com.au/
http://galavorn.com/
Obviously, I will need to grow to that size of a site but I love it...
1.Client Sign in portal-
2. Social media and blog friendly!! I want people to use the site on a regular. I will post video, articles, and social media daily.
visitors can sign up or in using social media
very open to suggestions
Landing page for site that allows visitor to decide what they want to visit (button)- should be catchy
a. Convention & Meeting Services
b. Social Events
c. Small Business Solutions
2. Tabs
a. Home (ability to have pic gallery rotating)
b. About MLG
c. Contact us
d. Convention & Meeting services
e. Social Events
f. Small Business Solutions
g. Testimonials
Nice to have
- Mobile friendly, very clean design

```html
<!DOCTYPE html>
<html lang="en">
<head>
<meta charset="utf-8">
<title>Marigold Logistics &amp; Gatherings</title>
<link rel="stylesheet" href="https://fonts.googleapis.com/css2?family=Ubuntu:wght@400;500;700&family=Open+Sans:ital,wght@0,300;0,400;1,300&display=swap">
<style>
:root{
  --purple:#5b45a8;
  --nav-top:#b9a7ea;
  --nav-bottom:#8c6fd6;
  --red:#d3281c;
  --ink:#2b2b2b;
  --text:#555;
  --muted:#8a8a8a;
  --line:#e3e3e3;
  --panel:#fafafa;
  --footer:#f1f1f1;
}
*{box-sizing:border-box;margin:0;padding:0}
html,body{width:850px;height:1200px;overflow:hidden;background:#fff}
body{position:relative;font-family:"Open Sans",Arial,sans-serif;color:var(--text)}
.abs{position:absolute}
h1,h2,h3,h4,.nav a,.brand{font-family:"Ubuntu",Arial,sans-serif;font-weight:400}

/* header */
.brand{left:48px;top:20px;width:170px;display:flex;align-items:center;gap:8px;color:var(--purple);font-size:15px;line-height:18px;font-weight:500}
.brand-dot{width:14px;height:14px;border-radius:50%;background:var(--purple);flex:none}
.top-links{right:48px;top:10px;font-size:10px;color:#777}
.top-links span{margin:0 4px;color:#aaa}
.search{left:590px;top:42px;width:218px;height:26px;border:1px solid #ddd;font-size:9.5px;font-style:italic;color:#999;padding:6px 10px}
.search svg{position:absolute;right:8px;top:5px}

/* nav */
.nav{left:41px;top:82px;width:771px;height:41px;background:linear-gradient(var(--nav-top),var(--nav-bottom));border-radius:4px 4px 0 0;display:flex;align-items:center;padding-left:21px}
.nav a{color:#fff;text-decoration:none;font-size:12.5px;font-weight:500;padding:0 15px;border-left:1px solid rgba(255,255,255,.35);line-height:18px}
.nav a:first-child{border-left:0;padding-left:0}

/* hero */
.hero{left:41px;top:123px;width:771px;height:272px;border:1px solid var(--line);border-top:0;border-radius:0 0 4px 4px;background:radial-gradient(ellipse at 40% 40%,#fff 40%,#ececec 100%)}
.hero h1{position:absolute;left:63px;top:50px;color:var(--red);font-size:29px;font-weight:700;line-height:34px}
.hero h2{position:absolute;left:63px;top:84px;color:var(--red);font-size:21px;line-height:26px}
.hero p{position:absolute;left:63px;top:116px;width:290px;font-size:10.5px;line-height:19px;color:#777}
.dots{position:absolute;left:65px;top:188px;display:flex;gap:3px}
.dots i{width:10px;height:10px;border-radius:50%;background:#bbb}
.dots i:first-child{background:#111}
.arrow{position:absolute;top:94px}
.photo{position:absolute;background:#fff;padding:5px;box-shadow:0 2px 6px rgba(0,0,0,.3)}
.photo div{width:100%;height:100%}

/* content */
.welcome h2{left:46px;top:426px;color:var(--purple);font-size:19.5px}
.lead{left:46px;top:457px;width:500px;font-size:11px;color:var(--ink)}
.intro{left:46px;top:478px;width:500px;font-size:9.4px;line-height:17.6px;color:#555}
.section-title{font-size:16.5px;color:#444}
.event{width:158px}
.event .pic{height:99px}
.event h4{font-size:11px;color:var(--ink);margin-top:10px}
.event p{font-size:9px;line-height:13.6px;color:#777;margin-top:2px}
.event small{display:block;font-size:9px;color:#444;margin-top:4px}

.box{border:1px solid var(--line);border-radius:3px;background:#fff}
.box h3{font-size:17px;color:var(--purple)}
.box .red-title{color:var(--red)}
.service{display:flex;gap:8px;margin-top:17px}
.service .pic{width:70px;height:59px;flex:none}
.service h4{font-family:"Open Sans",Arial,sans-serif;font-size:9.3px;color:var(--ink);font-weight:400}
.service p{font-size:8.4px;line-height:13.7px;color:#999;margin-top:2px}
.quote{font-size:9.4px;line-height:15.3px;color:#999;font-style:italic;font-weight:300}
.author{font-size:9.4px;color:#666;margin-top:6px}

.gallery{display:grid;grid-template-columns:repeat(3,66px);gap:6px 8px;margin-top:10px}
.gallery div{height:54px}
.feed{left:328px;top:853px;width:206px;height:163px;border:1px solid var(--line);background:#fff;padding:10px 28px 0 15px;overflow:hidden}
.feed h4{font-family:"Open Sans",Arial,sans-serif;font-size:9.5px;color:var(--ink);font-weight:400}
.feed p{font-size:8.6px;line-height:13.8px;color:#888;margin-bottom:10px}
.scroll{position:absolute;right:2px;top:2px;width:12px;height:157px;border-left:1px solid #eee}
.follow{left:421px;top:1023px;font-size:8px;color:#444;letter-spacing:.2px;display:flex;align-items:center;gap:5px;white-space:nowrap}

/* footer */
.footer{left:0;top:1088px;width:850px;height:112px;background:var(--footer)}
.footer-links{position:absolute;left:46px;top:25px;font-size:11px;color:#444}
.footer-links span{margin:0 5px;color:#888}
.copyright{position:absolute;left:46px;top:51px;font-size:9px;color:#555}
.social{position:absolute;left:736px;top:27px;display:flex;gap:8px}
.social i{width:20px;height:20px;border-radius:50%;background:#666}
</style>
</head>
<body>

<header>
  <div class="abs brand"><span class="brand-dot"></span><span>Marigold Logistics &amp; Gatherings</span></div>
  <div class="abs top-links">Become Member<span>|</span>Login<span>|</span>Register<span>|</span>FAQ</div>
  <div class="abs search">Search here..
    <svg width="14" height="14" viewBox="0 0 14 14"><circle cx="6" cy="6" r="4.3" fill="none" stroke="#777" stroke-width="1.8"/><line x1="9.2" y1="9.2" x2="13" y2="13" stroke="#777" stroke-width="2.2" stroke-linecap="round"/></svg>
  </div>
  <nav class="abs nav">
    <a>Home</a><a>About Us</a><a>Convention &amp; Meeting Services</a><a>Social Events</a><a>Small Business</a><a>Testimonials</a>
  </nav>
</header>

<section class="abs hero">
  <h1>Join Our Planning</h1>
  <h2>and Events Now</h2>
  <p>Inullamcorper, est eget tempor cursus, neque mi consectetuer mi, a ultricies massa est sed nisl. Class aptent taciti sociosqu ad litora torquent</p>
  <div class="dots"><i></i><i></i><i></i><i></i></div>
  <svg class="arrow" style="left:18px" width="22" height="50" viewBox="0 0 22 50"><polyline points="20,2 2,25 20,48" fill="none" stroke="#aaa" stroke-width="1.5"/></svg>
  <svg class="arrow" style="left:740px" width="22" height="50" viewBox="0 0 22 50"><polyline points="2,2 20,25 2,48" fill="none" stroke="#aaa" stroke-width="1.5"/></svg>

  <div class="photo" style="left:392px;top:28px;width:280px;height:215px;transform:rotate(-3deg)"><div style="background:linear-gradient(135deg,#8b6a4a,#c9a47a)"></div></div>
  <div class="photo" style="left:422px;top:43px;width:298px;height:190px"><div role="img" aria-label="Photo of a cheering crowd of fans with pom-poms" style="background:linear-gradient(135deg,#e05a2a,#e8c340 45%,#3a6fb0)"></div></div>
  <div class="photo" style="left:411px;top:128px;width:156px;height:116px;transform:rotate(2deg)"><div role="img" aria-label="Photo of guests celebrating at a party" style="background:linear-gradient(135deg,#3a2420,#a34a3a 55%,#e0b080)"></div></div>
</section>

<main>
  <section class="welcome">
    <h2 class="abs">Welcome to Our Website Mainpage</h2>
    <p class="abs lead">Mauris vel lacus vitae felis vestibulum volutpat. Etiam est nunc, venenatis in, tristique eu</p>
    <p class="abs intro">Phasellus felis dolor, scelerisque a, tempus eget, lobortis id, libero. Donec scelerisque leo ac risus. Praesent sit amet est. In dictum, dolor eu dictum porttitor, enim felis viverra mi, eget luctus massa purus quis odio. Etiam nulla massa, pharetra facilisis, volutpat in, imperdiet sit amet, sem. Aliquam nec erat at purus cursus interdum.</p>
  </section>

  <h3 class="abs section-title" style="left:45px;top:566px">Upcoming Events</h3>
  <article class="abs event" style="left:45px;top:595px">
    <div class="pic" role="img" aria-label="Photo of a woman laughing at a festive dinner" style="background:linear-gradient(135deg,#6a4a3a,#d8b08a 60%,#f0e0c8)"></div>
    <h4>Event Tittle here</h4>
    <p>Nunc tempus felis vitae urna. Vivamus porttitor, g, purus nisi eleifend libero, a tempus libero</p>
    <small>2 hour ago | 0 Comments</small>
  </article>
  <article class="abs event" style="left:215px;top:595px">
    <div class="pic" role="img" aria-label="Photo of a couple dancing at a nightclub event" style="background:linear-gradient(135deg,#1a1210,#7a3a2a 55%,#d09070)"></div>
    <h4>Event Tittle here</h4>
    <p>Nunc tempus felis vitae urna. Vivamus porttitor, g, purus nisi eleifend libero, a tempus libero</p>
    <small>2 hour ago | 0 Comments</small>
  </article>
  <article class="abs event" style="left:386px;top:595px">
    <div class="pic" role="img" aria-label="Photo of friends gathered around a laptop" style="background:linear-gradient(135deg,#4a7aa8,#e8e4dc 55%,#c89070)"></div>
    <h4>Event Tittle here</h4>
    <p>Nunc tempus felis vitae urna. Vivamus porttitor, g, purus nisi eleifend libero, a tempus libero</p>
    <small>2 hour ago | 0 Comments</small>
  </article>

  <section class="abs box" style="left:44px;top:816px;width:250px;height:228px;padding:20px 19px">
    <h3 class="red-title">Featured Gallery</h3>
    <div class="gallery">
      <div role="img" aria-label="Photo of a dinner party" style="background:linear-gradient(135deg,#2a1a12,#9a6a40)"></div>
      <div role="img" aria-label="Photo of a speaker at a conference" style="background:linear-gradient(135deg,#c8d0dc,#5a6a80)"></div>
      <div role="img" aria-label="Photo of a business meeting" style="background:linear-gradient(135deg,#9aa8a0,#3a4a50)"></div>
      <div role="img" aria-label="Photo of a couple toasting" style="background:linear-gradient(135deg,#e8d8c8,#a07858)"></div>
      <div role="img" aria-label="Photo of a group celebrating" style="background:linear-gradient(135deg,#3a2010,#c88a30)"></div>
      <div role="img" aria-label="Photo of a team working together" style="background:linear-gradient(135deg,#e8e8ee,#3a5a8a)"></div>
      <div role="img" aria-label="Photo of colourful party drinks" style="background:linear-gradient(135deg,#e06a20,#e8c030)"></div>
      <div role="img" aria-label="Photo of red paper lanterns" style="background:linear-gradient(135deg,#5a1a10,#d02a18)"></div>
      <div role="img" aria-label="Photo of a networking event" style="background:linear-gradient(135deg,#d8d8d8,#5a5a60)"></div>
    </div>
  </section>

  <section class="abs box" style="left:316px;top:815px;width:230px;height:229px;background:var(--panel);padding:15px 15px">
    <h3 class="red-title">Chirper Feed</h3>
  </section>
  <div class="abs feed">
    <h4>Nunc tempus felis</h4>
    <p>Vivamus porttitor, g, purus nisi eleifend libero, a tempus libero</p>
    <h4>Duis sed tellus et</h4>
    <p>Vivamus porttitor, g, purus nisi eleifend libero, a tempus libero</p>
    <h4>Nulla elementum dui</h4>
    <p>Vivamus porttitor, g, purus nisi eleifend</p>
    <svg class="scroll" viewBox="0 0 12 157" preserveAspectRatio="none">
      <rect x="0" y="0" width="12" height="12" fill="#dde6f2" stroke="#8aa0c0"/>
      <polygon points="3,8 9,8 6,4" fill="#3a5a90"/>
      <rect x="0.5" y="78" width="11" height="26" fill="#dde6f2" stroke="#8aa0c0"/>
      <line x1="4" y1="88" x2="8" y2="88" stroke="#3a5a90"/><line x1="4" y1="91" x2="8" y2="91" stroke="#3a5a90"/><line x1="4" y1="94" x2="8" y2="94" stroke="#3a5a90"/>
      <rect x="0" y="145" width="12" height="12" fill="#dde6f2" stroke="#8aa0c0"/>
      <polygon points="3,149 9,149 6,153" fill="#3a5a90"/>
    </svg>
  </div>
  <div class="abs follow">
    <svg width="9" height="9" viewBox="0 0 9 9"><polygon points="0,4.5 9,0 6,9" fill="#d3281c"/></svg>
    FOLLOW US ON CHIRPER
  </div>

  <aside class="abs box" style="left:570px;top:413px;width:248px;height:282px;padding:12px 17px">
    <h3>Service Provide</h3>
    <div class="service" style="margin-top:10px">
      <div class="pic" role="img" aria-label="Photo of an audience at a seminar" style="background:linear-gradient(135deg,#3a2a24,#b07050)"></div>
      <div><h4>Phasellus felis dolor</h4><p>Donec convallis pede venenatis nibh. Duis quam. Nam eget lacus. Aliquam erat volutpat.</p></div>
    </div>
    <div class="service">
      <div class="pic" role="img" aria-label="Photo of a concert crowd under blue lights" style="background:linear-gradient(135deg,#8ad0f0,#1a4a90 60%,#0a1a30)"></div>
      <div><h4>Class aptent taciti</h4><p>Donec convallis pede venenatis nibh. Duis quam. Nam eget lacus. Aliquam erat volutpat.</p></div>
    </div>
    <div class="service">
      <div class="pic" role="img" aria-label="Photo of guests at a formal gala" style="background:linear-gradient(135deg,#2a1a1a,#8a5a60)"></div>
      <div><h4>Ut ac mi quis</h4><p>Donec convallis pede venenatis nibh. Duis quam. Nam eget lacus. Aliquam erat volutpat.</p></div>
    </div>
  </aside>

  <aside class="abs box" style="left:570px;top:706px;width:248px;height:336px;padding:16px 20px">
    <h3>Testimonials</h3>
    <p class="quote" style="margin-top:10px">Class aptent taciti sociosqu ad litora torquent per conubia nostra, per inceptos hymenaeos. Proin nulla arcu, nonummy luctus, dictum eget, fermentum et, lorem. Nunc porta convallis pede.</p>
    <p class="author">By Author Name</p>
    <p class="quote" style="margin-top:20px">Donec iaculis diam a nisi accumsan viverra. Duis sed tellus et tortor vestibulum gravida. Praesent elementum elit at tellus</p>
    <p class="author">By Author Name</p>
    <p class="quote" style="margin-top:20px">Class aptent taciti sociosqu ad litora torquent per conubia nostra, per inceptos hymenaeos. Proin nulla arcu, nonummy luctus, dictum eget, fermentum et, lorem. Nunc porta convallis pede.</p>
    <p class="author">By Author Name</p>
  </aside>
</main>

<footer class="abs footer">
  <div class="footer-links">Home<span>|</span>About MLG<span>|</span>Contact us<span>|</span>Convention &amp; Meeting services<span>|</span>Social Events<span>|</span>Small Business Solutions<span>|</span>Testimonials</div>
  <div class="copyright">© 2013 Company Name. All right reserved. Term of Use</div>
  <div class="social"><i></i><i></i><i></i></div>
</footer>

</body>
</html>
```